Business card design for Sable Crestway

We need business cards designed for our new marketing consulting company, Sable Crestway. Our services include marketing strategy, go-to-market and launch planning, growth strategy, and execution. We serve medical technology and health technology companies, from startups to well-established growth companies.

The business cards should feel professional, credible, reliable and trustworthy, and should instill confidence. Also bold, creative, and modern.

The design must use the Sable Crestway logo.

The primary brand color is this orange: #FF5501
A secondary color that you can use is this gray: #282B2D
I would prefer only to use the orange and gray. But if you feel you really need an additional accent color (please use it very sparingly, as little as possible), you can use this blue for small accent purposes: #009FED

Attached are the logo files. The main logo is the one with a little bit of orange on the left and the rest is gray.

The business card should include the following:

Sable Crestway logo
First name and last name
Title
Email address
Phone number and type (in whatever order looks best for the design
Website (the website does not need to be in the same block as the personal info)

For example:

Wren Tasker
Founder & Principal
wren@sablecrestway.com
+1.415.836.2094 mobile (can use "." or spaces in between blocks of numbers)
sablecrestway.com (somewhere on the card, it does not need to be with the personal info; and note that there is no "www." at the beginning)

Note that there will be no address listed on the business card.

Target Market(s)

Executives (CEO, head of marketing, head of sales) at medical technology and health technology companies, mostly in their 40s and older, well-educated, often with advanced degrees. They are strategic thinkers, responsible for budgets, and familiar with P&L. Their comfort with and trust in using outside consultants varies.

Industry/Entity Type

Medical technology and health technology companies.

Contact Information for Business Card

See project description

Font styles to use
Sans Serif

Requirements
Must have
• Logo and see Business card details section above.

```html
<!DOCTYPE html>
<html lang="en">
<head>
<meta charset="utf-8">
<title>Sable Crestway — Business Card</title>
<link rel="stylesheet" href="https://fonts.googleapis.com/css2?family=Michroma&family=Montserrat:wght@400;500;700&display=swap">
<style>
  :root {
    --brand-orange: #FF5501;
    --brand-gray: #282B2D;
    --card-white: #FFFFFF;
    --page-bg: #3A3C3E;
    --wordmark-font: "Michroma", sans-serif;
    --body-font: "Montserrat", sans-serif;
  }
  * { box-sizing: border-box; margin: 0; padding: 0; }
  html, body {
    width: 1200px; height: 900px; overflow: hidden;
    background: var(--page-bg);
  }
  .canvas {
    position: relative; width: 1200px; height: 900px;
  }
  .card {
    position: absolute; left: 250px; width: 700px; height: 400px;
    border-radius: 26px; overflow: hidden;
  }
  /* Back */
  .card-back {
    top: 30px; background: var(--brand-orange);
    display: flex; align-items: center; justify-content: center; gap: 26px;
  }
  .brand-dot {
    width: 70px; height: 70px; border-radius: 50%;
    border: 9px solid var(--card-white);
  }
  .brand-name {
    font-family: var(--wordmark-font);
    font-size: 40px; line-height: 1.15; letter-spacing: 10px;
    text-transform: uppercase; color: var(--card-white);
  }
  /* Front */
  .card-front {
    top: 470px; background: var(--card-white);
  }
  .front-brand {
    position: absolute; top: 50px; left: 0; right: 0;
    display: flex; align-items: center; justify-content: center; gap: 22px;
  }
  .front-brand .brand-dot { border-color: var(--brand-gray); width: 62px; height: 62px; border-width: 8px; }
  .front-brand .brand-name { color: var(--brand-gray); font-size: 34px; letter-spacing: 9px; }
  .person {
    position: absolute; top: 182px; left: 70px; width: 240px; text-align: right;
  }
  .person-name {
    font-family: var(--wordmark-font);
    font-size: 22px; letter-spacing: 4px; color: var(--brand-orange);
    text-transform: uppercase;
  }
  .person-title {
    font-family: var(--body-font); font-size: 15px; color: var(--brand-gray);
    margin-top: 4px;
  }
  .divider {
    position: absolute; top: 176px; left: 330px; width: 2px; height: 76px;
    background: var(--brand-orange);
  }
  .contact {
    position: absolute; top: 176px; left: 346px; list-style: none;
    font-family: var(--body-font); font-size: 16px; color: var(--brand-gray);
  }
  .contact li { display: flex; align-items: center; gap: 7px; height: 25px; }
  .contact svg { width: 13px; height: 13px; flex: none; }
  .contact .accent { color: var(--brand-orange); }
  .rule {
    position: absolute; left: 0; right: 0; top: 270px; height: 2px;
    background: var(--brand-gray);
  }
  .service-band {
    position: absolute; left: 0; right: 0; top: 278px; bottom: 0;
    background: var(--brand-orange);
    display: flex; flex-direction: column; justify-content: center; align-items: center;
    font-family: var(--body-font); font-size: 18px; color: var(--card-white);
    line-height: 1.5;
  }
</style>
</head>
<body>
<main class="canvas">
  <section class="card card-back">
    <span class="brand-dot"></span>
    <span class="brand-name">Sable<br>Crestway</span>
  </section>

  <section class="card card-front">
    <div class="front-brand">
      <span class="brand-dot"></span>
      <span class="brand-name">Sable<br>Crestway</span>
    </div>

    <div class="person">
      <p class="person-name">Wren Tasker</p>
      <p class="person-title">Founder &amp; Principal</p>
    </div>

    <div class="divider"></div>

    <ul class="contact">
      <li>
        <svg viewBox="0 0 16 16"><path fill="#FF5501" d="M3.5 1l3 3-1.7 1.9c.9 2 2.3 3.4 4.3 4.3L11 8.5l3 3-2 2.5C6.5 13.5 2.5 9.5 1 3.5z"/></svg>
        +1.415.836.2094
      </li>
      <li>
        <svg viewBox="0 0 16 16"><rect x="1" y="3" width="14" height="10" fill="none" stroke="#FF5501" stroke-width="1.8"/><path d="M1 3l7 6 7-6" fill="none" stroke="#FF5501" stroke-width="1.8"/></svg>
        wren@sablecrestway.com
      </li>
      <li>
        <svg viewBox="0 0 16 16"><circle cx="8" cy="8" r="7" fill="none" stroke="#FF5501" stroke-width="1.6"/><ellipse cx="8" cy="8" rx="3" ry="7" fill="none" stroke="#FF5501" stroke-width="1.3"/><path d="M1 8h14" stroke="#FF5501" stroke-width="1.3"/></svg>
        <span>www.<span class="accent">sablecrestway</span>.com</span>
      </li>
    </ul>

    <div class="rule"></div>

    <div class="service-band">
      <p>marketing strategy &nbsp;|&nbsp; go-to-market and launch planning</p>
      <p>growth strategy, and execution</p>
    </div>
  </section>
</main>
</body>
</html>
```